Velora Aesthetica

Medical doctor providing aesthetic medicine

* Double sided card
* Logo to be on card
Other details:
* Dr. Mirela Kostvan, BSc, MBChB, CCFP
* #214-215, 27903 83 Ave, Surrey, BC, V2T 4K7
* 604-718-2943
* info@veloraclinic.ca
* www.veloraclinic.ca

Industry/Entity Type

Medical / Health & Beauty

Contact Information for Business Card

see 'Project Description'

Colors
0054AA
0677BA
7BADD7
CADEEF
E8F1F8
FFF300
FFF600
FEFA6F
FFFEC7
FFFEE8

Requirements
Must have
• Modern, high-end design

```html
<!DOCTYPE html>
<html lang="en">
<head>
<meta charset="utf-8">
<title>Velora Aesthetica – Business Card</title>
<link href="https://fonts.googleapis.com/css2?family=Montserrat:wght@400;500&family=Encode+Sans+Condensed:wght@400;500&display=swap" rel="stylesheet">
<style>
  :root {
    --navy: #1d4166;
    --navy-pattern: #1f5688;
    --gold: #e2b52a;
    --ink: #1c2f4d;
    --paper: #ffffff;
    --pattern-light: #eceef4;
    --backdrop: #eeebe6;
  }
  * { box-sizing: border-box; margin: 0; padding: 0; }
  html, body {
    width: 1200px; height: 900px; overflow: hidden;
    background: var(--backdrop);
  }
  .sheet {
    width: 1200px; height: 900px;
    display: flex; align-items: center; justify-content: center; gap: 40px;
  }
  .card {
    position: relative;
    width: 540px; height: 309px;
    overflow: hidden;
    box-shadow: 0 10px 28px rgba(60, 40, 20, 0.22);
  }

  /* Front */
  .card--front { background: var(--navy); }
  .card--front .pattern-field {
    position: absolute; inset: 0;
    background: linear-gradient(100deg, var(--navy-pattern) 0%, rgba(31,86,136,0.55) 45%, rgba(29,65,102,0) 75%);
  }
  .brand {
    position: absolute;
    display: flex; align-items: center; gap: 14px;
  }
  .card--front .brand {
    inset: 0;
    justify-content: center;
  }
  .brand__circle {
    width: 40px; height: 40px; border-radius: 50%;
    border: 2px solid var(--gold);
    flex: none;
  }
  .brand__name {
    font-family: "Montserrat", sans-serif;
    font-weight: 400;
    font-size: 19px;
    letter-spacing: 0.24em;
    text-transform: uppercase;
    white-space: nowrap;
  }
  .card--front .brand__name { color: var(--paper); }

  /* Back */
  .card--back { background: var(--paper); }
  .card--back .pattern-field {
    position: absolute; left: 0; top: 0; bottom: 0; width: 300px;
    background: linear-gradient(90deg, var(--pattern-light) 0%, rgba(236,238,244,0.6) 60%, rgba(255,255,255,0) 100%);
  }
  .tab {
    position: absolute; top: 0; right: 34px;
    width: 20px; height: 42px; background: var(--gold);
  }
  .card--back .brand { left: 28px; top: 196px; gap: 9px; }
  .card--back .brand__circle { width: 26px; height: 26px; }
  .card--back .brand__name { color: var(--ink); font-size: 12px; letter-spacing: 0.2em; }

  .contact {
    position: absolute; left: 300px; top: 48px;
    font-family: "Encode Sans Condensed", sans-serif;
    color: var(--ink);
  }
  .contact__name {
    font-size: 24px; font-weight: 500;
    padding-bottom: 6px;
    border-bottom: 2px solid var(--gold);
    display: inline-block;
  }
  .contact__credentials {
    font-size: 14px; margin: 6px 0 14px 46px;
  }
  .contact__list { list-style: none; font-size: 14px; line-height: 1.45; }
  .contact__item { display: flex; align-items: flex-start; gap: 8px; }
  .contact__icon { width: 12px; height: 12px; margin-top: 3px; flex: none; fill: var(--gold); }
</style>
</head>
<body>
<main class="sheet">
  <section class="card card--front" aria-label="Card front">
    <div class="pattern-field" role="img" aria-label="Subtle blue triangle texture"></div>
    <div class="brand">
      <span class="brand__circle"></span>
      <span class="brand__name">Velora Aesthetica</span>
    </div>
  </section>

  <section class="card card--back" aria-label="Card back">
    <div class="pattern-field" role="img" aria-label="Faint grey triangle texture"></div>
    <div class="tab"></div>
    <div class="brand">
      <span class="brand__circle"></span>
      <span class="brand__name">Velora Aesthetica</span>
    </div>
    <div class="contact">
      <h1 class="contact__name">Dr. Mirela Kostvan</h1>
      <p class="contact__credentials">BSc, MBChB, CCFP</p>
      <ul class="contact__list">
        <li class="contact__item">
          <svg class="contact__icon" viewBox="0 0 12 12" aria-hidden="true"><path d="M6 0a4 4 0 0 0-4 4c0 3 4 8 4 8s4-5 4-8a4 4 0 0 0-4-4zm0 5.5A1.5 1.5 0 1 1 6 2.5a1.5 1.5 0 0 1 0 3z"/></svg>
          <span>#214-215, 27903 83 Ave<br>Surrey, BC, V2T 4K7</span>
        </li>
        <li class="contact__item">
          <svg class="contact__icon" viewBox="0 0 12 12" aria-hidden="true"><path d="M2.5 0.5l2 2.5-1.2 1.3c.8 1.7 2 2.9 3.7 3.7L8.3 6.8l2.7 2-1 2.7C5 11 1 7 .5 2z"/></svg>
          <span>604-718-2943</span>
        </li>
        <li class="contact__item">
          <svg class="contact__icon" viewBox="0 0 12 12" aria-hidden="true"><path d="M0 2h12v8H0zM1 3l5 4 5-4z" fill-rule="evenodd"/></svg>
          <span>info@veloraclinic.ca</span>
        </li>
        <li class="contact__item">
          <svg class="contact__icon" viewBox="0 0 12 12" aria-hidden="true"><circle cx="6" cy="6" r="5.5"/><path d="M0.5 6h11M6 0.5c-2 2.5-2 8.5 0 11M6 0.5c2 2.5 2 8.5 0 11" stroke="#fff" stroke-width="0.9" fill="none"/></svg>
          <span>www.veloraclinic.ca</span>
        </li>
      </ul>
    </div>
  </section>
</main>
</body>
</html>
```